Business Card for premium dental clinic

We are a premium dental clinic based in Brasov, Romania with more than 15 year on the market, providing quality dental treatment made by a team of more specialized dentists, working with modern equipment as a solution to beautiful and healthy teeth.

Our current logo for the clinic use 2 square with colors black and gold - dr Corbescu - studio, using family fonts Bodoni, Myriad Pro and Segoe Print.
Depending on the printing we used some gold CMYK background or gold foil picture background or a gold gradient.
We want a business card:
- eye catching business card
- distinguished business card
- premium design
- to keep the color scheme of black and gold
- to attract the customers to spent time reading the information
- modern concept

```html
<!DOCTYPE html>
<html lang="en">
<head>
<meta charset="utf-8">
<title>dr Corbescu Studio – Business Card</title>
<link href="https://fonts.googleapis.com/css2?family=Oswald:wght@300;400&family=Open+Sans:wght@400;600&display=swap" rel="stylesheet">
<style>
  :root {
    --stage: #2a2c2f;
    --card-black: #0d0d0d;
    --card-graphite: #2b2b2b;
    --gold-light: #f7d56a;
    --gold: #e0a923;
    --gold-deep: #9c6a12;
    --ink-light: #e9e9e9;
    --ink-muted: #bdbdbd;
    --white: #ffffff;
  }
  * { box-sizing: border-box; margin: 0; padding: 0; }
  html, body { width: 1200px; height: 900px; overflow: hidden; }
  body {
    background: var(--stage);
    display: flex;
    flex-direction: column;
    align-items: center;
    justify-content: center;
    gap: 56px;
    font-family: "Open Sans", sans-serif;
  }

  .card {
    width: 560px;
    height: 320px;
    position: relative;
    overflow: hidden;
    box-shadow: 0 18px 40px rgba(0,0,0,.45);
  }

  /* Front */
  .card-front {
    background: var(--card-black);
    border: 6px solid var(--white);
    display: flex;
  }
  .foil-panel {
    width: 46%;
    height: 100%;
    background:
      radial-gradient(circle at 30% 30%, var(--gold-light), transparent 55%),
      radial-gradient(circle at 75% 75%, var(--gold-light), transparent 50%),
      linear-gradient(135deg, var(--gold) 0%, var(--gold-deep) 45%, var(--gold) 70%, var(--gold-deep) 100%);
  }
  .front-identity {
    flex: 1;
    display: flex;
    flex-direction: column;
    justify-content: center;
    padding-left: 34px;
  }
  .brand-name {
    font-family: "Oswald", sans-serif;
    font-weight: 300;
    font-size: 40px;
    line-height: 1.15;
    color: var(--white);
  }
  .tagline {
    font-family: "Oswald", sans-serif;
    font-weight: 300;
    font-size: 30px;
    color: var(--white);
    margin-top: 34px;
    letter-spacing: .5px;
  }

  /* Back */
  .card-back {
    background: linear-gradient(160deg, #353535 0%, var(--card-graphite) 55%, #1f1f1f 100%);
    border: 5px solid var(--gold);
    display: flex;
    align-items: center;
    padding: 0 40px;
  }
  .back-identity {
    width: 210px;
    display: flex;
    align-items: center;
    gap: 10px;
  }
  .brand-mark {
    width: 18px; height: 18px;
    background: var(--gold);
    flex: none;
  }
  .back-identity .brand-name { font-size: 22px; }
  .divider {
    width: 1px;
    height: 130px;
    margin: 0 34px 0 16px;
    background: linear-gradient(to bottom, transparent, rgba(255,255,255,.55), transparent);
  }
  .contact-list { list-style: none; display: flex; flex-direction: column; gap: 10px; }
  .contact-item {
    display: flex;
    align-items: flex-start;
    gap: 12px;
    font-size: 13px;
    color: var(--ink-light);
    line-height: 1.4;
  }
  .contact-icon {
    width: 20px; height: 20px;
    border-radius: 50%;
    background: var(--gold-light);
    flex: none;
    display: flex; align-items: center; justify-content: center;
  }
  .contact-icon svg { width: 12px; height: 12px; }
  .address-city { color: var(--ink-muted); }
</style>
</head>
<body>

  <section class="card card-front">
    <div class="foil-panel" role="img" aria-label="Crumpled gold foil texture"></div>
    <div class="front-identity">
      <p class="brand-name">dr. Corbescu Studio</p>
      <p class="tagline">dental clinic</p>
    </div>
  </section>

  <section class="card card-back">
    <div class="back-identity">
      <span class="brand-mark"></span>
      <p class="brand-name">dr. Corbescu Studio</p>
    </div>
    <div class="divider"></div>
    <ul class="contact-list">
      <li class="contact-item">
        <span class="contact-icon"><svg viewBox="0 0 12 12"><path d="M2.5 1h2l1 2.5-1.3 1a6 6 0 0 0 3.3 3.3l1-1.3 2.5 1v2c0 .6-.4 1-1 1A9.5 9.5 0 0 1 1.5 2c0-.6.4-1 1-1z" fill="#1a1a1a"/></svg></span>
        +40 268 555 019
      </li>
      <li class="contact-item">
        <span class="contact-icon"><svg viewBox="0 0 12 12"><rect x="1" y="2.5" width="10" height="7" fill="none" stroke="#1a1a1a" stroke-width="1.2"/><path d="M1 2.5l5 4 5-4" fill="none" stroke="#1a1a1a" stroke-width="1.2"/></svg></span>
        contact@drcorbescu.ro
      </li>
      <li class="contact-item">
        <span class="contact-icon"><svg viewBox="0 0 12 12"><circle cx="6" cy="6" r="4.8" fill="none" stroke="#1a1a1a" stroke-width="1.1"/><ellipse cx="6" cy="6" rx="2" ry="4.8" fill="none" stroke="#1a1a1a" stroke-width="1"/><path d="M1.2 6h9.6" stroke="#1a1a1a" stroke-width="1"/></svg></span>
        www.drcorbescu.ro
      </li>
      <li class="contact-item">
        <span class="contact-icon"><svg viewBox="0 0 12 12"><path d="M6 11S2 6.8 2 4.5a4 4 0 0 1 8 0C10 6.8 6 11 6 11z" fill="#1a1a1a"/><circle cx="6" cy="4.5" r="1.4" fill="#f7d56a"/></svg></span>
        <span>Strada Lunga nr 48<br><span class="address-city">Brasov, Romania</span></span>
      </li>
    </ul>
  </section>

</body>
</html>
```